Commercial Construction Interior Fitout company needs Logo and Business Cards

We need a logo and business card design. We specialise in Commercial Ceilings, Partitions, Plastering and Carpentry.

Company name: 7QX Commercial Interiors. Would like a professional looking card more than a fancy look. Gloss front preferably black pattern with Fluro Green and white text.

Will need:

Name
Position
Phone
Fax
Email
Postal Address
Web address
Updates

Thank you so much everyone for your efforts and fantastic designs..   If I didn't respond to everyone personally,  my apologises. 

Again, thanks all

R.M                               

Target Market(s)

Existing & New clients in the Construction Industry

Industry/Entity Type

Business

Requirements
Nice to have
• 7QX to be overlapped or made into some sort of Logo

```html
<!DOCTYPE html>
<html lang="en">
<head>
<meta charset="utf-8">
<title>7QX Commercial Interiors – Business Card</title>
<link rel="stylesheet" href="https://fonts.googleapis.com/css2?family=Oswald:wght@600&family=Source+Sans+3:wght@400;700&display=swap">
<style>
  :root {
    --stage: #e9e7e4;
    --green: #3f9d45;
    --green-deep: #1f6e2c;
    --green-bright: #6ec43c;
    --white: #ffffff;
    --paper-shade: #d6d6d6;
    --ink: #1b1b1b;
    --ink-soft: #333333;
  }
  html, body {
    margin: 0;
    width: 1200px;
    height: 1200px;
    overflow: hidden;
    background: var(--stage);
  }
  .canvas {
    position: relative;
    width: 1200px;
    height: 1200px;
  }
  .card {
    position: absolute;
    left: 150px;
    width: 900px;
    height: 514px;
    box-shadow: 0 10px 30px rgba(0,0,0,.18);
    overflow: hidden;
  }
  /* front */
  .card-front {
    top: 60px;
    background: radial-gradient(ellipse at 50% 45%, var(--green-bright) 0%, var(--green) 45%, var(--green-deep) 100%);
    display: flex;
    align-items: center;
    justify-content: center;
  }
  .brand {
    display: flex;
    align-items: center;
    gap: 22px;
    font-family: "Source Sans 3", sans-serif;
    font-weight: 700;
    color: var(--ink);
  }
  .brand-dot {
    border-radius: 50%;
    background: var(--white);
    flex: none;
  }
  .card-front .brand { font-size: 58px; }
  .card-front .brand-dot { width: 70px; height: 70px; }

  /* back */
  .card-back {
    top: 626px;
    background: linear-gradient(100deg, var(--white) 55%, var(--paper-shade) 100%);
  }
  .card-back .brand {
    position: absolute;
    top: 70px;
    right: 50px;
    font-size: 30px;
    gap: 14px;
  }
  .card-back .brand-dot {
    width: 34px; height: 34px;
    background: var(--green);
  }
  .person {
    position: absolute;
    left: 80px;
    top: 80px;
  }
  .person-name {
    margin: 0;
    font-family: "Oswald", sans-serif;
    font-weight: 600;
    font-size: 52px;
    line-height: 1;
    color: var(--green-bright);
    text-transform: uppercase;
  }
  .person-role {
    margin: 6px 0 0;
    font-family: "Source Sans 3", sans-serif;
    font-size: 22px;
    color: var(--ink-soft);
  }
  .contact {
    position: absolute;
    left: 80px;
    top: 240px;
    margin: 0;
    padding: 0;
    list-style: none;
    font-family: "Source Sans 3", sans-serif;
    font-size: 21px;
    line-height: 28px;
    color: var(--green);
  }
  .contact li { display: flex; align-items: center; gap: 12px; }
  .contact svg { width: 16px; height: 16px; fill: var(--green); flex: none; }
  .band {
    position: absolute;
    left: 0; right: 0; bottom: 0;
    height: 130px;
    background: linear-gradient(90deg, var(--green-deep), var(--green) 50%, var(--green-deep));
  }
</style>
</head>
<body>
<main class="canvas">

  <section class="card card-front" aria-label="Card front">
    <div class="brand"><span class="brand-dot"></span><span>7QX Commercial Interiors</span></div>
  </section>

  <section class="card card-back" aria-label="Card back">
    <div class="person">
      <h1 class="person-name">Daniel Harper</h1>
      <p class="person-role">Managing Director</p>
    </div>

    <div class="brand"><span class="brand-dot"></span><span>7QX Commercial Interiors</span></div>

    <ul class="contact">
      <li><svg viewBox="0 0 16 16"><path d="M3 1l3 3-1.5 2a9 9 0 0 0 5.5 5.5L12 10l3 3-2 2C7 15 1 9 1 3z"/></svg>+10 555 0142</li>
      <li><svg viewBox="0 0 16 16"><path d="M4 1h8v4H4zM1 6h14v7h-3v2H4v-2H1zm4 5v3h6v-3z"/></svg>+10 555 0143</li>
      <li><svg viewBox="0 0 16 16"><path d="M1 3h14v2L8 9 1 5zm0 4l7 4 7-4v6H1z"/></svg>hello@7qxcommercial.com</li>
      <li><svg viewBox="0 0 16 16"><path d="M6 10l4-4M5 8L3 10a2.5 2.5 0 0 0 3.5 3.5L8 11M11 8l2-2A2.5 2.5 0 0 0 9.5 2.5L8 5" stroke="#3f9d45" stroke-width="2" fill="none"/></svg>www.7qxcommercial.com</li>
      <li><svg viewBox="0 0 16 16"><path d="M8 1a5 5 0 0 0-5 5c0 4 5 9 5 9s5-5 5-9a5 5 0 0 0-5-5zm0 3a2 2 0 1 1 0 4 2 2 0 0 1 0-4z"/></svg>45 Sample Road, Riverton, Westland</li>
    </ul>

    <div class="band"></div>
  </section>

</main>
</body>
</html>
```